Jewelry Wholesale Business Card Design

Company name: VELORA
Business Background: Wholesale jewelry store located in downtown Los Angeles. We specialize in 18k gold-filled, stainless steel, 14kt gold, and natural stone jewelry.
website: www.velorashop.example
Instagram: velora_
Email: sales@velorashop.example
Address: 318 W. PRIOR ST #27, #109
LOS ANGELES, CA 90099
(213)555-0147

We would like to create a simple, yet elegant business card for my store
-Includes company logo
-Black background preferred
-Gold metallic color letters
- Lists the type of products we sell
-Small icons for instagram handle, phone, email, and website

Target Market(s)

Hispanic community, age 12-40

Industry/Entity Type

Jewelry Wholesale

Contact Information for Business Card

logo, business location, website, phone number, email, instagram, lists type of products, Dylan Morvet(my name)

Font styles to use
Serif
Sans Serif

Colors
FFF300
FFF600
FEFA6F
FFFEC7
FFFEE8

Requirements
Must have
• logo, business location, website, phone number, email, instagram, lists type of products, Dylan Morvet(my name)

```html
<!DOCTYPE html>
<html lang="en">
<head>
<meta charset="utf-8">
<title>VELORA Business Card</title>
<link rel="stylesheet" href="https://fonts.googleapis.com/css2?family=Cormorant+Garamond:wght@500&family=Roboto:wght@400;500&display=swap">
<style>
  :root {
    --backdrop: #1b1b1d;
    --card-dark: #1f2022;
    --card-mid: #3a3c40;
    --card-back: #232426;
    --gold: #d38a2e;
    --gold-light: #e9a94f;
    --text: #ffffff;
    --muted: #c9c9c9;
    --photo-shadow: #2b2a28;
  }
  * { box-sizing: border-box; margin: 0; padding: 0; }
  html, body {
    width: 1200px; height: 960px; overflow: hidden;
    background: var(--backdrop);
  }
  .card {
    position: absolute; left: 240px;
    width: 720px; height: 411px;
    overflow: hidden;
    box-shadow: 0 16px 40px rgba(0,0,0,0.6);
  }
  .card-front {
    top: 46px;
    background: linear-gradient(160deg, var(--card-mid) 0%, #2c2d30 35%, var(--card-dark) 75%);
  }
  .card-back {
    top: 503px;
    background: linear-gradient(150deg, #2e2f32 0%, var(--card-back) 45%, #161719 100%);
    display: flex; align-items: center; justify-content: center;
  }
  .product-photo {
    position: absolute; left: 338px; top: 122px;
    width: 382px; height: 238px;
    background:
      radial-gradient(ellipse 60% 45% at 58% 50%, rgba(196,156,78,0.85) 0%, rgba(138,106,46,0.55) 45%, rgba(43,42,40,0) 80%),
      linear-gradient(90deg, rgba(31,32,34,0) 0%, var(--photo-shadow) 40%, var(--card-dark) 100%);
    -webkit-mask-image: linear-gradient(90deg, transparent 0%, #000 25%, #000 85%, transparent 100%);
            mask-image: linear-gradient(90deg, transparent 0%, #000 25%, #000 85%, transparent 100%);
  }
  .brand {
    position: absolute; left: 50px; top: 40px;
    display: flex; align-items: center; gap: 18px;
  }
  .brand-mark {
    width: 50px; height: 50px; border-radius: 50%;
    background: var(--gold);
  }
  .brand-name {
    font-family: "Cormorant Garamond", serif;
    font-weight: 500; font-size: 34px; letter-spacing: 2px;
    color: var(--text);
  }
  .contact-list { position: absolute; list-style: none; }
  .contact-list.social { left: 50px; top: 150px; }
  .contact-list.location { left: 310px; top: 282px; }
  .contact-item {
    display: flex; align-items: flex-start; gap: 12px;
    font-family: "Roboto", sans-serif; font-weight: 500;
    font-size: 16px; line-height: 21px; color: var(--text);
    margin-bottom: 9px;
  }
  .icon {
    flex: none; width: 23px; height: 23px; border-radius: 50%;
    background: radial-gradient(circle at 35% 30%, var(--gold-light), var(--gold));
    display: flex; align-items: center; justify-content: center;
    margin-top: -1px;
  }
  .icon svg { width: 13px; height: 13px; }
  .owner {
    position: absolute; left: 50px; top: 236px;
    font-family: "Cormorant Garamond", serif; font-weight: 500;
    font-size: 22px; color: var(--gold-light); letter-spacing: 1px;
  }
  .product-list {
    position: absolute; left: 50px; top: 272px; list-style: none;
    font-family: "Roboto", sans-serif; font-weight: 400;
    font-size: 12px; line-height: 19px; letter-spacing: 1px;
    color: var(--muted);
  }
  .product-list li::before { content: "• "; color: var(--gold); }
  .back-brand {
    display: flex; align-items: center; gap: 20px;
  }
  .back-brand .brand-mark { width: 64px; height: 64px; }
  .back-brand .brand-name { font-size: 44px; color: var(--gold-light); letter-spacing: 4px; }
</style>
</head>
<body>
  <section class="card card-front" aria-label="VELORA business card front">
    <div class="product-photo" role="img" aria-label="Photograph of two gold engagement rings with diamonds"></div>

    <header class="brand">
      <span class="brand-mark" aria-hidden="true"></span>
      <span class="brand-name">VELORA</span>
    </header>

    <ul class="contact-list social">
      <li class="contact-item">
        <span class="icon" aria-hidden="true"></span>
        <span>velora_</span>
      </li>
      <li class="contact-item">
        <span class="icon" aria-hidden="true">
          <svg viewBox="0 0 24 24"><rect x="2" y="5" width="20" height="14" rx="1.5" fill="#fff"/><path d="M2.5 6 L12 13 L21.5 6" fill="none" stroke="#d38a2e" stroke-width="1.8"/></svg>
        </span>
        <span>sales@velorashop.example</span>
      </li>
    </ul>

    <p class="owner">Dylan Morvet</p>
    <ul class="product-list">
      <li>18K GOLD-FILLED</li>
      <li>STAINLESS STEEL</li>
      <li>14KT GOLD</li>
      <li>NATURAL STONE</li>
    </ul>

    <ul class="contact-list location">
      <li class="contact-item">
        <span class="icon" aria-hidden="true">
          <svg viewBox="0 0 24 24" fill="none" stroke="#fff" stroke-width="1.8"><circle cx="12" cy="12" r="9"/><ellipse cx="12" cy="12" rx="4" ry="9"/><path d="M3 12h18M5 7h14M5 17h14"/></svg>
        </span>
        <span>www.velorashop.example</span>
      </li>
      <li class="contact-item">
        <span class="icon" aria-hidden="true">
          <svg viewBox="0 0 24 24"><path d="M12 2a7 7 0 0 0-7 7c0 5 7 13 7 13s7-8 7-13a7 7 0 0 0-7-7z" fill="#fff"/><circle cx="12" cy="9" r="2.6" fill="#d38a2e"/></svg>
        </span>
        <span>318 W. PRIOR ST #27, #109<br>LOS ANGELES, CA 90099<br>(213)555-0147</span>
      </li>
    </ul>
  </section>

  <section class="card card-back" aria-label="VELORA business card back">
    <div class="back-brand">
      <span class="brand-mark" aria-hidden="true"></span>
      <span class="brand-name">VELORA</span>
    </div>
  </section>
</body>
</html>
```